Simple and clean

We need a business card design for a new company called Dwelling Owl. It is a search engine to find current properties for sale or rent in New Zealand market.
We have already a colour scheme that we would like people to use.
Light brown: #D4CCB0
Light green: #D6E4D4
Green: #669966
Black/White
It is OK to divert from this colour scheme slightly as long as there is a green component to the business card.
Final design should be clean, simple and should communicate the nature of the business.
Target Market(s)
- First home buyers
- Real estate agents
- People seeking rentals
Industry/Entity Type
Business
Requirements
Must have
- Use those or similar colours.
Light brown: #D4CCB0
Light green: #D6E4D4
Green: #669966
Black/White

```html
<!DOCTYPE html>
<html lang="en">
<head>
<meta charset="utf-8">
<title>Dwelling Owl – Business Card</title>
<link rel="stylesheet" href="https://fonts.googleapis.com/css2?family=Arimo&family=Cinzel:wght@400&family=Open+Sans:wght@700&display=swap">
<style>
  :root {
    --light-brown: #D4CCB0;
    --light-green: #D6E4D4;
    --green: #669966;
    --texture-dark: #8a9c8c;
    --texture-light: #b7c6b7;
    --white: #ffffff;
    --black: #111111;
  }
  html, body {
    margin: 0;
    padding: 0;
    width: 1200px;
    height: 734px;
    overflow: hidden;
    background: var(--white);
  }
  .card {
    position: relative;
    width: 1200px;
    height: 734px;
    overflow: hidden;
    background: var(--white);
  }
  .band { position: absolute; left: 0; width: 100%; }
  .band--top-rule { top: 0; height: 42px; background: var(--light-brown); }
  .band--header { top: 42px; height: 235px; background: var(--white); }
  .band--mid-rule { top: 277px; height: 45px; background: var(--light-brown); }
  .band--texture {
    background: linear-gradient(160deg, var(--texture-light) 0%, #a3b4a4 45%, var(--texture-dark) 100%);
  }
  .band--contact-panel { top: 322px; height: 268px; }
  .band--web { top: 590px; height: 84px; background: var(--white); }
  .band--bottom-rule { top: 674px; height: 23px; background: var(--light-brown); }
  .band--footer { top: 697px; height: 37px; }

  .brand-mark {
    position: absolute;
    left: 60px;
    top: 40px;
    width: 372px;
    height: 372px;
  }

  .brand-name {
    position: absolute;
    left: 450px;
    top: 128px;
    margin: 0;
    font-family: "Cinzel", serif;
    font-weight: 400;
    font-size: 66px;
    line-height: 1;
    letter-spacing: 3px;
    color: var(--black);
    white-space: nowrap;
  }

  .contact {
    position: absolute;
    left: 483px;
    top: 350px;
    color: var(--black);
  }
  .contact__name {
    margin: 0;
    font-family: "Open Sans", sans-serif;
    font-weight: 700;
    font-size: 56px;
    line-height: 64px;
    letter-spacing: -0.5px;
  }
  .contact__line {
    margin: 0;
    font-family: "Arimo", sans-serif;
    font-size: 41px;
    line-height: 66px;
    word-spacing: 12px;
    letter-spacing: 0.5px;
    white-space: nowrap;
  }

  .website {
    position: absolute;
    left: 32px;
    top: 603px;
    margin: 0;
    font-family: "Arimo", sans-serif;
    font-size: 45px;
    line-height: 54px;
    letter-spacing: 1.5px;
    color: var(--green);
  }
</style>
</head>
<body>
  <div class="card">
    <div class="band band--top-rule"></div>
    <div class="band band--header"></div>
    <div class="band band--mid-rule"></div>
    <div class="band band--texture band--contact-panel" role="img" aria-label="Scratched grey-green stone texture"></div>
    <div class="band band--web"></div>
    <div class="band band--bottom-rule"></div>
    <div class="band band--texture band--footer" role="img" aria-label="Scratched grey-green stone texture"></div>

    <svg class="brand-mark" viewBox="0 0 372 372" aria-hidden="true">
      <circle cx="186" cy="186" r="186" fill="var(--light-green)"/>
    </svg>

    <h1 class="brand-name">Dwelling Owl</h1>

    <div class="contact">
      <p class="contact__name">Name</p>
      <p class="contact__line">Job title</p>
      <p class="contact__line">Mobile no. &amp; email address</p>
    </div>

    <p class="website">www.dwellingowl.co.nz</p>
  </div>
</body>
</html>
```